Cyber Security Site Design (Products & Consulting)

I need my website redesigned to be engaging, clean, efficient and modern. My company (when its up and running) is going to be concentrated on two things: a few specific products for cyber security as well as cyber security consulting services. The background I bring to the field is having worked with small companies all the way to the largest government organizations and advising them on their security posture and how to improve it. We need the ability to add products and services easily.

For a sample product, you can use either Heron (http://www.heron-relay.example/) or Vorlant Greystone (https://www.vorlant.example/products/relay-hub-and-layered-access-portal).

It will replace https://talmerocharts.example/

Target Market(s)

Cyber Security professionals in all verticals

Coding

Coded - Design and coding required

Number of Pages Required

4 page

Font styles to use
Sans Serif

Colors
6b449b

Requirements
Must have
• Ability to easily modify
• Have main page
• Have product specific pages
• Have consulting services pages
• Have executive team information
• Clean, modern design
• Usage of the logo and its color scheme
Nice to have
• I like the idea of a left collapsed sidebar (so icons only) that can expand for text.
• I am also open to a very unique landing page, possibly a shape in the middle (hexagons maybe?) with each of the options there.
Should not have
• Nothing that looks like it came out of a hacker movie

```html
<!DOCTYPE html>
<html lang="en">
<head>
<meta charset="utf-8">
<title>Talmero Charts — Cyber Security Consulting &amp; Products</title>
<link rel="stylesheet" href="https://fonts.googleapis.com/css2?family=Exo+2:wght@400;500;600;700&family=Montserrat:wght@400;500;600;700&display=swap">
<style>
:root{
  --purple:#6b449b;
  --purple-dark:#4f2f7a;
  --purple-deep:#3d2260;
  --ink:#2b2b2b;
  --text:#6a6a6a;
  --muted:#9a9a9a;
  --grey-bg:#f1f1f1;
  --node:#4a4a4a;
  --charcoal:#2f2f33;
  --white:#ffffff;
  --line:#d9d9d9;
}
*{box-sizing:border-box;margin:0;padding:0}
html,body{width:1200px;height:3846px;overflow:hidden}
body{position:relative;background:var(--white);font-family:"Montserrat",sans-serif;color:var(--text)}
h1,h2,h3{font-family:"Exo 2",sans-serif}

/* header */
.site-header{position:absolute;left:0;top:0;width:1200px;height:72px;background:var(--white);display:flex;align-items:center;padding:0 140px}
.brand{display:flex;align-items:center;gap:10px;font-family:"Exo 2",sans-serif;font-weight:700;font-size:24px;color:var(--purple);letter-spacing:.5px}
.brand .mark{width:26px;height:26px;background:var(--purple);border-radius:4px}
.main-nav{margin-left:auto;display:flex;align-items:center;gap:34px;font-size:12px;font-weight:600;color:var(--ink)}
.main-nav .active{color:var(--purple)}
.pill{display:inline-flex;align-items:center;gap:8px;background:var(--purple);color:var(--white);border-radius:20px;padding:8px 18px;font-size:12px;font-weight:600}
.pill .dot{width:16px;height:16px;border-radius:50%;background:var(--white)}

/* hero */
.hero{position:absolute;left:0;top:72px;width:1200px;height:673px;overflow:hidden}
.hero-photo{position:absolute;inset:0;background:linear-gradient(180deg,#1a2a55 0%,#2d3f72 35%,#5a4a5e 62%,#2a2230 100%)}
.hero-title{position:absolute;left:0;top:195px;width:1200px;text-align:center;color:var(--white);font-family:"Exo 2",sans-serif;font-weight:600;font-size:46px;letter-spacing:.5px}
.hero-sub{position:absolute;left:0;top:256px;width:1200px;text-align:center;color:var(--white);font-size:17px}
.hero-cta{position:absolute;left:513px;top:308px;font-size:11px}
.hero-bands{position:absolute;left:0;top:0}
.band-label{position:absolute;color:var(--white);font-family:"Exo 2",sans-serif;font-weight:500;font-size:25px;line-height:29px;text-transform:uppercase}
.band-icon{position:absolute;width:58px;height:58px;border:2px solid var(--white);border-radius:50%}

/* about */
.section-title{position:absolute;left:0;width:1200px;text-align:center;font-family:"Exo 2",sans-serif;font-size:40px;color:var(--ink);font-weight:400}
.section-title b{font-weight:700}
.section-title::after{content:"";display:block;width:44px;height:4px;background:var(--purple);margin:16px auto 0}
.about-heading{position:absolute;left:141px;top:820px;display:flex;align-items:center;gap:14px;font-family:"Exo 2",sans-serif;font-size:42px;font-weight:500;color:var(--ink)}
.about-heading .brand{font-size:40px}
.about-copy{position:absolute;left:141px;top:905px;width:465px;font-size:11px;line-height:17px}
.about-copy p{margin-bottom:12px}
.about-copy strong{color:var(--purple);font-weight:700}
.about-copy .lead{color:var(--ink);font-weight:600}
.about-cta{position:absolute;left:141px;top:1218px;font-size:11px}
.portrait-frame{position:absolute;left:692px;top:820px;width:360px;height:436px;border:14px solid #cfcfcf;border-radius:0 34px 0 34px}
.portrait-frame::before{content:"";position:absolute;left:-14px;top:-14px;width:60px;height:200px;border-left:14px solid var(--purple);border-top:14px solid var(--purple)}
.portrait-frame::after{content:"";position:absolute;right:-14px;bottom:-14px;width:200px;height:60px;border-right:14px solid var(--purple);border-bottom:14px solid var(--purple);border-radius:0 0 34px 0}
.portrait{position:absolute;left:718px;top:846px;width:308px;height:384px;background:linear-gradient(180deg,#e9ecef 0%,#cfd4da 55%,#3a4250 100%)}
.exec-name{position:absolute;left:692px;top:1265px;width:360px;text-align:center;color:var(--ink);font-weight:600;font-size:15px}
.exec-role{position:absolute;left:692px;top:1289px;width:360px;text-align:center;font-size:10px;color:var(--text)}

/* services */
.services{position:absolute;left:0;top:1325px;width:1200px;height:585px;background:var(--grey-bg)}
.services-intro{position:absolute;left:230px;top:1478px;width:740px;text-align:center;font-size:12px;line-height:19px}
.services-intro strong,.services-intro em{color:var(--purple);font-style:normal}
.services-intro .lead{color:var(--ink);font-weight:600;margin-bottom:12px}
.service-row{position:absolute;left:141px;top:1628px;width:915px;height:217px;background:var(--white);display:flex}
.service-card{position:relative;width:183px;padding:24px 14px 0;text-align:center}
.service-card h3{font-family:"Montserrat",sans-serif;font-size:13px;font-weight:600;color:var(--ink);line-height:17px;margin:14px 0 10px}
.service-card p{font-size:10px;line-height:14px;color:var(--muted)}
.service-card .icon{width:46px;height:46px;margin:0 auto}
.service-card.is-active{background:var(--purple);margin-top:-18px;height:250px;border-radius:10px 10px 0 0;padding-top:42px}
.service-card.is-active h3,.service-card.is-active p{color:var(--white)}
.service-card .more{display:block;margin-top:12px;color:var(--white);font-size:10px;font-weight:700}
.slider-arrow{position:absolute;top:1714px;width:30px;height:30px;border-radius:50%;background:var(--white);box-shadow:0 1px 4px rgba(0,0,0,.15)}

/* products */
.product-hub{position:absolute;left:0;top:0}
.product-node{position:absolute;width:82px;height:82px;margin:-41px 0 0 -41px;border-radius:50%;background:var(--node)}
.product-node.is-featured{background:var(--purple);border:5px solid #d6c8e8}
.product-label{position:absolute;font-size:13px;font-weight:600;color:var(--ink);line-height:17px}
.product-label.is-featured{color:var(--purple)}

/* team */
.team{position:absolute;left:0;top:2659px;width:1200px;height:636px;background:linear-gradient(180deg,#1c1c20 0%,#2c2c34 60%,#1d1d22 100%)}
.team .section-title{color:var(--white)}
.team-card{position:absolute;top:2833px;width:262px;height:347px;background:var(--white);border-radius:0 28px 0 28px;overflow:hidden}
.team-photo{height:222px;background:linear-gradient(180deg,#eef0f3 0%,#c9ced6 60%,#2f3947 100%)}
.team-card .name{text-align:center;color:var(--ink);font-weight:600;font-size:15px;margin-top:20px}
.team-card .role{text-align:center;font-size:10px;margin-top:6px}
.team-card.is-open{background:var(--purple)}
.team-card.is-open .team-photo{height:190px}
.team-card.is-open .name,.team-card.is-open .role{color:var(--white)}
.team-card.is-open .name{margin-top:22px}
.team-contact{color:var(--white);font-size:14px;font-weight:600;padding:14px 0 0 70px;line-height:28px}
.team-contact small{font-size:11px;font-weight:500}

/* footer */
.contact{position:absolute;left:0;top:3295px;width:1200px;height:500px;background:var(--purple)}
.contact-brand{position:absolute;left:0;top:3318px;width:1200px;display:flex;justify-content:center}
.contact-brand .brand{color:var(--white);font-size:40px}
.contact-brand .mark{width:40px;height:40px;background:var(--white)}
.cta-title{position:absolute;left:141px;top:3407px;font-family:"Exo 2",sans-serif;font-size:34px;color:var(--white);font-weight:500;letter-spacing:.5px}
.cta-title::after{content:"";display:block;width:44px;height:3px;background:var(--white);margin-top:4px}
.cta-text{position:absolute;left:141px;top:3470px;width:360px;font-size:12px;line-height:17px;color:var(--white)}
.contact h4,.contact-details h4,.quick-links h4{font-size:13px;color:var(--white);font-weight:600}
.contact-details{position:absolute;left:141px;top:3545px;width:240px;color:var(--white);font-size:11px;line-height:16px}
.contact-details li{list-style:none;display:flex;gap:10px;margin-top:14px}
.contact-details .phone{font-size:17px;font-weight:700}
.contact-details svg{flex:none;margin-top:2px}
.quick-links{position:absolute;left:400px;top:3545px;color:var(--white);font-size:11px}
.quick-links ul{list-style:none;margin-top:14px;line-height:18px}
.quick-links li::before{content:"›";margin-right:10px}
.contact-form{position:absolute;left:615px;top:3410px;width:441px;height:385px;background:var(--white);padding:28px 46px}
.field{height:38px;border:1px solid var(--line);margin-bottom:12px;font-size:11px;color:var(--muted);padding:11px 12px}
.field.tall{height:58px}
.submit{margin-top:8px;font-size:11px}
.legal{position:absolute;left:0;top:3795px;width:1200px;height:51px;background:var(--purple-deep);display:flex;align-items:center;padding:0 141px;color:var(--white);font-size:11px}
.legal b{font-weight:700}
.social{margin-left:auto;display:flex;gap:8px}
.social span{width:26px;height:26px;border-radius:50%;border:1.5px solid var(--white)}
</style>
</head>
<body>

<header class="site-header">
  <div class="brand"><span class="mark"></span>Talmero Charts</div>
  <nav class="main-nav">
    <span class="active">HOME</span><span>ABOUT</span><span>OUR TEAM</span><span>OUR PRODUCTS</span><span>SERVICES</span>
    <span class="pill"><span class="dot"></span>CONTACT US</span>
  </nav>
</header>

<section class="hero">
  <div class="hero-photo" role="img" aria-label="City skyline at night with light trails on a highway"></div>
  <h1 class="hero-title">CYBER SECURITY CONSULTING &amp; PRODUCTS</h1>
  <p class="hero-sub">A full range of Cyber Security Consulting Services and Products to meet your business requirements</p>
  <span class="pill hero-cta"><span class="dot"></span>GET STARTED NOW!</span>
  <svg class="hero-bands" width="1200" height="673" viewBox="0 0 1200 673">
    <polygon points="0,428 600,518 600,673 0,673" fill="#6b449b"/>
    <polygon points="1200,428 600,518 600,673 1200,673" fill="#2f2f33"/>
    <path d="M0,673 L0,655 Q600,580 1200,655 L1200,673 Z" fill="#ffffff"/>
    <circle cx="600" cy="564" r="42" fill="#ffffff"/>
    <circle cx="600" cy="564" r="24" fill="none" stroke="#6b449b" stroke-width="5"/>
  </svg>
  <span class="band-icon" style="left:138px;top:535px"></span>
  <div class="band-label" style="left:215px;top:535px">Cyber Security<br>Consulting Services</div>
  <div class="band-label" style="left:790px;top:535px;text-align:right">Cyber Security<br>Products</div>
  <span class="band-icon" style="left:998px;top:535px"></span>
</section>

<section class="about">
  <h2 class="about-heading">ABOUT <span class="brand"><span class="mark" style="width:36px;height:36px"></span>Talmero Charts</span></h2>
  <div class="about-copy">
    <p class="lead"><strong>TALMERO CHARTS</strong> It is a long established fact that a reader will be distracted by the readable content of a page when looking at its layout. The point of using Lorem Ipsum</p>
    <p>It is a long established fact that a reader will be distracted by the readable content of a page when looking at its layout. The point of using Lorem Ipsum is that it has a more-or-less normal distribution of letters, as opposed to using 'Content here, content here', making it look like readable English. Many desktop publishing packages and web page editors now use Lorem Ipsum as their default model text, and a search for 'lorem ipsum' will uncover many web sites still in their infancy. Various versions have evolved over the years</p>
    <p>The point of using Lorem Ipsum is that it has a more-or-less normal distribution of letters, as opposed to using 'Content here, content here', making it look like readable English. Many desktop publishing packages and web page editors now use Lorem Ipsum</p>
  </div>
  <span class="pill about-cta"><span class="dot"></span>READ MORE</span>
  <div class="portrait-frame"></div>
  <div class="portrait" role="img" aria-label="Portrait of the founder and CEO in a suit"></div>
  <p class="exec-name">Mr. Martin Kessler Oberland</p>
  <p class="exec-role">Founder &amp; CEO</p>
</section>

<section class="services"></section>
<h2 class="section-title" style="top:1384px">OUR <b>SERVICES</b></h2>
<div class="services-intro">
  <p class="lead"><strong>TALMERO CHARTS</strong> It is a long established fact that a reader will be distracted by the readable content of a page when looking at its layout. The point of using Lorem Ipsum is that it has a more-or-less normal distribution of letters</p>
  <p>The point of using Lorem Ipsum is that it has a more-or-less <em>TALMERO CHARTS</em> normal distribution of letters, as opposed to using 'Content here, content here', making it look like readable English</p>
</div>
<span class="slider-arrow" style="left:67px"></span>
<span class="slider-arrow" style="left:1096px"></span>
<div class="service-row">
  <article class="service-card">
    <svg class="icon" viewBox="0 0 46 46" fill="none" stroke="#6b449b" stroke-width="2"><rect x="5" y="8" width="36" height="26" rx="2"/><path d="M5 14h36M16 40h14M23 34v6"/><circle cx="23" cy="24" r="5"/></svg>
    <h3>Cyber Security<br>Services</h3>
    <p>The point of using Lorem Ipsum is that it has point more-or-lessmaking that itlook like readable</p>
  </article>
  <article class="service-card">
    <svg class="icon" viewBox="0 0 46 46" fill="none" stroke="#6b449b" stroke-width="2"><path d="M10 4h20l8 8v30H10z"/><path d="M30 4v8h8"/><path d="M23 18l8 3v6c0 5-4 8-8 9-4-1-8-4-8-9v-6z"/></svg>
    <h3>Managed Security<br>Services</h3>
    <p>The point of using Lorem Ipsum is that it has point more-or-lessmaking that itlook like readable</p>
  </article>
  <article class="service-card is-active">
    <svg class="icon" viewBox="0 0 46 46" fill="none" stroke="#ffffff" stroke-width="2"><path d="M23 6c-9 0-15 6-15 14 0 5 3 8 3 12v6h24v-6c0-4 3-7 3-12 0-8-6-14-15-14z"/><path d="M23 6v32M15 18h8M23 26h8"/></svg>
    <h3>Deep Slight<br>Intelligence</h3>
    <p>The point of using Lorem Ipsum is that it has point more-or-lessmaking that itlook like readable</p>
    <span class="more">READ MORE ››</span>
  </article>
  <article class="service-card">
    <svg class="icon" viewBox="0 0 46 46" fill="none" stroke="#6b449b" stroke-width="2"><path d="M6 40h34M10 40V28M18 40V22M26 40V26M34 40V16"/><path d="M8 22l10-8 8 6 12-12"/></svg>
    <h3>Incident Response<br>Services</h3>
    <p>The point of using Lorem Ipsum is that it has point more-or-lessmaking that itlook like readable</p>
  </article>
  <article class="service-card">
    <svg class="icon" viewBox="0 0 46 46" fill="none" stroke="#6b449b" stroke-width="2"><path d="M8 38l18-18M30 8a8 8 0 0 0-4 12l8 6a8 8 0 0 0 6-10l-5 4-5-5z"/><path d="M10 8l6 6M36 36L24 24"/></svg>
    <h3>Other<br>Services</h3>
    <p>The point of using Lorem Ipsum is that it has point more-or-lessmaking that itlook like readable</p>
  </article>
</div>

<section class="products">
  <h2 class="section-title" style="top:1974px">OUR <b>PRODUCTS</b></h2>
  <svg class="product-hub" width="1200" height="2660" viewBox="0 0 1200 2660">
    <circle cx="600" cy="2333" r="208" fill="none" stroke="#e6e6e6" stroke-width="2"/>
    <circle cx="600" cy="2333" r="120" fill="none" stroke="#d7d7d7" stroke-width="14"/>
    <path d="M600 2213 A120 120 0 0 1 704 2273" fill="none" stroke="#6b449b" stroke-width="14"/>
    <circle cx="600" cy="2333" r="100" fill="#ffffff"/>
    <circle cx="600" cy="2333" r="30" fill="#6b449b"/>
  </svg>
  <span class="product-node is-featured" style="left:600px;top:2123px"></span>
  <span class="product-node" style="left:751px;top:2197px"></span>
  <span class="product-node" style="left:803px;top:2333px"></span>
  <span class="product-node" style="left:751px;top:2479px"></span>
  <span class="product-node" style="left:600px;top:2538px"></span>
  <span class="product-node" style="left:441px;top:2479px"></span>
  <span class="product-node" style="left:390px;top:2333px"></span>
  <span class="product-node" style="left:449px;top:2192px"></span>
  <p class="product-label is-featured" style="left:652px;top:2102px">Integrated<br>Cyber Defense</p>
  <p class="product-label" style="left:805px;top:2180px">Advanced Threat<br>Protection</p>
  <p class="product-label" style="left:860px;top:2316px">Information<br>Protection</p>
  <p class="product-label" style="left:805px;top:2480px">Endpoint Security</p>
  <p class="product-label" style="left:652px;top:2541px">Email Security</p>
  <p class="product-label" style="left:258px;top:2472px">Network Security</p>
  <p class="product-label" style="left:226px;top:2326px">Cloud Security</p>
  <p class="product-label" style="left:278px;top:2175px;text-align:right">Small Business<br>Products</p>
</section>

<section class="team">
  <h2 class="section-title" style="top:87px">OUR <b>TEAM</b></h2>
</section>
<article class="team-card is-open" style="left:174px">
  <div class="team-photo" role="img" aria-label="Portrait of the marketing manager"></div>
  <p class="name">Mr. Aldo Ferrant</p>
  <p class="role">Marketing Manager</p>
  <div class="team-contact">
    <div>☎ 555 014 2291</div>
    <div><small>✉ info@aldo.example</small></div>
  </div>
</article>
<article class="team-card" style="left:469px">
  <div class="team-photo" role="img" aria-label="Portrait of the CEO"></div>
  <p class="name">Miss Lena Ferrant</p>
  <p class="role">C.E.O</p>
</article>
<article class="team-card" style="left:764px">
  <div class="team-photo" role="img" aria-label="Portrait of the marketing officer"></div>
  <p class="name">Mr. Theo Ferrant</p>
  <p class="role">Marketing Officer</p>
</article>

<footer class="contact"></footer>
<div class="contact-brand"><div class="brand"><span class="mark"></span>Talmero Charts</div></div>
<h2 class="cta-title">LET'S GET STARTED</h2>
<p class="cta-text">Take the first step to growing your business with a FREE consultation and quote.</p>
<div class="contact-details">
  <h4>Contact Details</h4>
  <ul>
    <li><svg width="12" height="14" viewBox="0 0 12 14"><path d="M6 0a5 5 0 0 0-5 5c0 4 5 9 5 9s5-5 5-9a5 5 0 0 0-5-5z" fill="#fff"/></svg><span><b>TALMERO CYBER SECURITY</b><br>418 Calder Row, Suite<br>#210 Marlow, TX 77990</span></li>
    <li><svg width="14" height="14" viewBox="0 0 14 14"><path d="M3 1l3 3-2 2c1 2 2 3 4 4l2-2 3 3-2 2C6 13 1 8 1 3z" fill="#fff"/></svg><span class="phone">555-014-2290</span></li>
    <li><svg width="14" height="12" viewBox="0 0 14 12"><rect x="0" y="1" width="14" height="10" fill="#fff"/><path d="M0 1l7 6 7-6" stroke="#6b449b" fill="none"/></svg><span>info@talmerocharts.example</span></li>
  </ul>
</div>
<div class="quick-links">
  <h4>Quick Links</h4>
  <ul><li>Home</li><li>About Us</li><li>Our Team</li><li>Our Products</li><li>Services</li><li>Contact</li></ul>
</div>
<form class="contact-form">
  <div class="field">First Name</div>
  <div class="field">Last Name</div>
  <div class="field">Email</div>
  <div class="field">Phone Number</div>
  <div class="field tall">Message</div>
  <span class="pill submit"><span class="dot"></span>SUBMIT</span>
</form>
<div class="legal">
  <span>Copyright © 2018 <b>TalmeroCharts</b>. All Right Reserved.</span>
  <span class="social"><span></span><span></span><span></span><span></span></span>
</div>

</body>
</html>
```